Packaging Design Project

We need a packaging design for a portable solar charger and 3-way cable.
The package style that is added in the pictures is preferred but we are open to suggestions.
I also added the cut line for the paper with fold lines

Industry/Entity Type

Solar

```html
<!DOCTYPE html>
<html lang="en">
<head>
<meta charset="utf-8">
<title>Solar Charger – Box Dieline</title>
<link rel="stylesheet" href="https://fonts.googleapis.com/css2?family=Michroma&display=swap">
<style>
  :root {
    --paper: #ffffff;
    --ink-dark: #0b0b0e;
    --ink-mid: #1c1d24;
    --panel-top: #101116;
    --band-light: #3a3f52;
    --band-dark: #15161c;
    --blue-strip: rgba(30, 90, 170, 0.55);
    --wave-a: #0d2f66;
    --wave-b: #3a86d6;
    --text-light: #e9ecf2;
    --text-soft: #b9bfcc;
    --cut-line: #e08a3c;
    --fold-line: #4a4d57;
  }
  * { margin: 0; padding: 0; box-sizing: border-box; }
  html, body { width: 1200px; height: 484px; overflow: hidden; background: var(--paper); }
  .canvas { position: relative; width: 1200px; height: 484px; font-family: "Michroma", sans-serif; font-variant: small-caps; color: var(--text-light); }

  .sleeve { position: absolute; left: 5px; top: 52px; width: 717px; height: 335px;
    background: linear-gradient(180deg, var(--panel-top) 0%, var(--ink-mid) 55%, var(--ink-dark) 100%); }
  .sleeve-band { position: absolute; left: 5px; top: 330px; width: 757px; height: 42px;
    background: linear-gradient(90deg, var(--band-dark) 0%, var(--band-light) 45%, var(--band-dark) 100%); }

  .wave-art { position: absolute; border-radius: 2px; }
  .wave-front { left: 5px; top: 92px; width: 340px; height: 100px;
    background: linear-gradient(180deg, transparent 0%, var(--wave-a) 35%, var(--wave-b) 55%, var(--wave-a) 75%, transparent 100%); opacity: .85; }
  .wave-back { left: 385px; top: 108px; width: 330px; height: 70px;
    background: linear-gradient(180deg, transparent 0%, #3b3e48 50%, transparent 100%); opacity: .8; }

  .blue-strip { position: absolute; left: 68px; top: 52px; width: 154px; height: 350px; background: var(--blue-strip); }
  .product-photo { position: absolute; left: 84px; top: 170px; width: 118px; height: 155px; border-radius: 10px;
    background: linear-gradient(160deg, #6d717c 0%, #1a1b20 45%, #2b2d33 100%); }

  .flip { position: absolute; transform: rotate(180deg); white-space: nowrap; }
  .headline { left: 70px; top: 336px; width: 250px; font-size: 22px; letter-spacing: 2px; text-align: center; }
  .subline { left: 170px; top: 318px; font-size: 7px; letter-spacing: 1px; color: var(--text-soft); }
  .tagline { left: 110px; top: 72px; font-size: 7px; letter-spacing: .8px; line-height: 11px; text-align: right; color: var(--text-soft); }

  .badge-circle { position: absolute; left: 240px; top: 221px; width: 66px; height: 66px; border-radius: 50%;
    border: 2px solid var(--text-soft); }
  .badge-name { left: 245px; top: 240px; width: 56px; text-align: center; font-size: 9px; line-height: 12px; }

  .vertical { position: absolute; transform: rotate(-90deg); transform-origin: left top; font-size: 10px; letter-spacing: 2px; white-space: nowrap; }
  .vertical-front { left: 356px; top: 318px; }
  .vertical-side { left: 737px; top: 318px; }

  .specs { left: 470px; top: 186px; font-size: 8px; line-height: 14.5px; letter-spacing: 1px; color: var(--text-soft); }
  .specs .specs-title { font-size: 11px; color: var(--text-light); letter-spacing: 2px; }

  .origin { left: 425px; top: 80px; font-size: 5.5px; letter-spacing: 1px; color: var(--text-soft); }
  .mark { position: absolute; border: 1.5px solid var(--text-soft); }
  .mark-round { left: 508px; top: 75px; width: 15px; height: 15px; border-radius: 50%; }
  .mark-square { left: 542px; top: 74px; width: 17px; height: 17px; background: #2c5b2a; border-color: #6fae5a; }
  .mark-round.second { left: 598px; }
  .mark-square.second { left: 650px; background: none; }

  .tray { position: absolute; left: 0; top: 0; }
</style>
</head>
<body>
<main class="canvas">
  <svg class="tray" width="1200" height="484" viewBox="0 0 1200 484" aria-hidden="true">
    <defs>
      <linearGradient id="trayFill" x1="0" y1="0" x2="0" y2="1">
        <stop offset="0" stop-color="#0e0f14"/>
        <stop offset="1" stop-color="#24262e"/>
      </linearGradient>
    </defs>
    <rect x="765" y="0" width="335" height="430" fill="url(#trayFill)"/>
    <rect x="722" y="52" width="423" height="335" fill="url(#trayFill)"/>
    <g fill="none" stroke="var(--fold-line)" stroke-width="1">
      <rect x="820" y="107" width="225" height="225"/>
      <rect x="852" y="140" width="158" height="158"/>
      <line x1="765" y1="52" x2="852" y2="140"/>
      <line x1="1100" y1="52" x2="1010" y2="140"/>
      <line x1="765" y1="387" x2="852" y2="298"/>
      <line x1="1100" y1="387" x2="1010" y2="298"/>
    </g>
    <g fill="none" stroke="var(--cut-line)" stroke-width="1">
      <polyline points="722,52 738,22 765,5 765,52"/>
      <polyline points="1100,5 1125,20 1145,52"/>
      <polyline points="722,52 722,387 765,387 765,430 810,472 1060,472 1100,430 1100,387 1145,387"/>
      <polyline points="1145,52 1195,120 1195,320 1145,387"/>
      <line x1="765" y1="52" x2="1145" y2="52"/>
      <line x1="765" y1="387" x2="1100" y2="387"/>
      <line x1="765" y1="0" x2="765" y2="430"/>
      <line x1="1100" y1="0" x2="1100" y2="430"/>
      <line x1="765" y1="0" x2="1100" y2="0"/>
    </g>
  </svg>

  <section class="sleeve"></section>
  <div class="wave-art wave-front" role="img" aria-label="Flowing blue light waves"></div>
  <div class="wave-art wave-back" role="img" aria-label="Faint grey light waves"></div>
  <div class="sleeve-band"></div>
  <div class="blue-strip"></div>
  <div class="product-photo" role="img" aria-label="Photo of the portable solar charger"></div>

  <p class="flip tagline">Portable solar charger for a Nimbo<br>with a 3-way USB charging cable</p>
  <p class="flip subline">With USB hub</p>
  <h1 class="flip headline">Solar Charger</h1>

  <div class="badge-circle"></div>
  <p class="flip badge-name">For<br>Nimbo</p>

  <p class="vertical vertical-front">Solar Charger</p>
  <p class="vertical vertical-side">Solar Charger</p>

  <div class="flip specs">
    <p class="specs-title">The specs:</p>
    <p>Capacity: 2200 mAh</p>
    <p>Input 5V-0.5A</p>
    <p>Output 5V-0.5A</p>
    <p>Charging time 3hours</p>
    <p>Standby time up to 230 hours</p>
    <p>Internet/talktime up to 4 hours on 3G</p>
    <p>Audio play up to 18 hours</p>
    <p>Video play up to 5 hours</p>
  </div>

  <p class="flip origin">Made in China</p>
  <span class="mark mark-round"></span>
  <span class="mark mark-square"></span>
  <span class="mark mark-round second"></span>
  <span class="mark mark-square second"></span>
</main>
</body>
</html>
```